Design a One Pager - About vTa

We are looking to produce a one pager that introduces our brand vTa in a nutshell (see www.vta.co.uk)
This should be on one page (not the back) and respect the vTa branding.
We have produced a one pager previously (here attached) but want to review the general design of it (in particular the graphs) and the content.
The new content is attached.
The first paragraph in the content file needs to be first.
Then there will be a title for the graph: Your Cloud Delivery Partner
We need a graph below that will be a mix of the one on the pager and of the green one attached. I have mocked up a draft version to show how it should look like in terms of placement / content.
This graph will show the following:
- entities on the left: head office / branch office / mobile working / home office / data centre. They all link to in the middle an entity with vTa: Network (preferably with the vTa logo) in the middle and below 'Enterprise WAN'
- Then below a link to another entity called Public internet.
- Then on the right 4 links to 4 different entities - one called Public Cloud (with logo nimbra data works / Quellon Skyview in it) / one called Private Cloud (with logo Tessvia in it) / one called SaaS / one called Cloud Telephony.
Below the graph there should be a list of bullet points about vTa (see content attached).
At the bottom there should be contact details (as seen on the original one pager) plus enough room to add some of our customers logos.
The colours of our brand are Pantone 432 / Pantone 549 but we're happy to introduce new colours in the mix (we sometimes use an orange - see website www.vta.co.uk) if they fit with the branding.
We have found some examples of one pagers that we like in style and because they don’t look too crowded.
https://uk.boardpinly.com/pin/582017364920184477/
http://morvadelacroix.com/?portfolio=bold-service-offerings-one-pager-draft-in-progress
https://www.deckvault.net/halvardmoensink/zepora-flyer-for-ktx-2013
Thank you

```html
<!DOCTYPE html>
<html lang="en">
<head>
<meta charset="utf-8">
<title>vTa – One Pager</title>
<link rel="stylesheet" href="https://fonts.googleapis.com/css2?family=Roboto:wght@400;500&family=Roboto+Condensed:wght@300;400;700&display=swap">
<style>
  :root {
    --brand-blue: #5b9bbf;
    --brand-blue-deep: #4a8ab0;
    --ink: #2a3036;
    --night: #070d18;
    --slate: #3a4753;
    --paper: #ffffff;
    --backdrop: #e8eaec;
    --line-grey: #4a4f55;
  }
  * { margin: 0; padding: 0; box-sizing: border-box; }
  html, body { width: 1200px; height: 1200px; overflow: hidden; background: var(--backdrop); }
  body { font-family: "Roboto", Arial, sans-serif; color: var(--ink); }

  .one-pager {
    position: absolute; left: 177px; top: 0;
    width: 846px; height: 1200px;
    background: var(--paper);
    box-shadow: 0 0 18px rgba(0,0,0,.18);
    overflow: hidden;
  }

  /* Header */
  .masthead { position: absolute; left: 0; top: 0; width: 846px; height: 114px; }
  .masthead__band { position: absolute; left: 0; top: 0; }
  .brand { position: absolute; left: 34px; top: 18px; }
  .brand__name { font-family: "Roboto", Arial, sans-serif; font-weight: 400; font-size: 80px; line-height: 1; color: var(--ink); }
  .contact-top { position: absolute; top: 55px; left: 558px; display: flex; align-items: center; gap: 6px; color: #fff; font-size: 13.5px; }
  .contact-top svg { display: block; }
  .contact-top .gap { width: 8px; }

  /* Intro */
  .intro { position: absolute; left: 0; top: 120px; width: 846px; height: 420px; background: var(--night); }
  .intro__copy { position: absolute; left: 35px; top: 64px; width: 384px; color: #fff; font-size: 14px; line-height: 20px; }
  .intro__copy p + p { margin-top: 20px; }
  .intro__copy .justify { text-align: justify; }
  .intro__visual {
    position: absolute; left: 425px; top: 0; width: 421px; height: 420px;
    background: radial-gradient(ellipse at 48% 62%, #4fb4ec 0%, #1f6aa6 28%, #0f2f52 55%, #070d18 85%);
  }

  /* Diagram section */
  .rule { position: absolute; left: 0; width: 846px; height: 6px; background: var(--brand-blue); }
  .headline { position: absolute; left: 60px; top: 588px; width: 230px; text-align: right; font-family: "Roboto Condensed", Arial, sans-serif; line-height: 1; }
  .headline span { display: block; }
  .headline .your { font-size: 98px; font-weight: 400; color: var(--ink); letter-spacing: -2px; }
  .headline .cloud { font-size: 74px; font-weight: 700; color: var(--brand-blue); margin-top: 2px; }
  .headline .delivery { font-size: 61px; font-weight: 400; color: var(--ink); margin-top: 8px; letter-spacing: -1px; }
  .headline .partner { font-size: 58px; font-weight: 700; color: var(--brand-blue); margin-top: 8px; }
  .headline-divider { position: absolute; left: 308px; top: 591px; width: 3px; height: 290px; background: var(--brand-blue); }
  .network-map { position: absolute; left: 0; top: 0; }
  .node-label { font-family: "Roboto Condensed", Arial, sans-serif; font-weight: 700; font-size: 10.5px; fill: var(--ink); text-anchor: middle; }
  .partner-name { font-family: "Roboto Condensed", Arial, sans-serif; font-weight: 700; font-size: 7.5px; fill: var(--line-grey); text-anchor: middle; }

  /* Highlights */
  .highlights { position: absolute; left: 0; top: 894px; width: 846px; height: 176px; background: var(--slate); }
  .highlights ul { position: absolute; top: 14px; list-style: none; color: #fff; font-size: 15px; }
  .highlights li { height: 34.4px; padding-left: 19px; position: relative; line-height: 20px; }
  .highlights li::before { content: ""; position: absolute; left: 0; top: 5px; width: 10px; height: 10px; border-radius: 50%; background: var(--brand-blue); }
  .highlights .col-a { left: 88px; }
  .highlights .col-b { left: 416px; }

  /* Footer */
  .footer { position: absolute; left: 0; top: 1147px; width: 846px; height: 53px; background: var(--brand-blue); display: flex; align-items: center; padding-left: 25px; color: #fff; }
  .footer__item { display: flex; align-items: center; gap: 4px; margin-right: 12px; white-space: nowrap; }
  .footer__item.small { font-size: 12px; }
  .footer__item.large { font-size: 15px; }
  .footer svg { display: block; }
</style>
</head>
<body>
<main class="one-pager">

  <header class="masthead">
    <svg class="masthead__band" width="846" height="114" viewBox="0 0 846 114">
      <polygon points="540,15 846,15 846,108 483,108" fill="var(--brand-blue)"/>
      <rect x="0" y="107" width="846" height="7" fill="var(--brand-blue)"/>
    </svg>
    <div class="brand">
      <div class="brand__name">vTa</div>
    </div>
    <div class="contact-top">
      <svg width="20" height="20" viewBox="0 0 20 20"><circle cx="10" cy="10" r="9" fill="none" stroke="#fff" stroke-width="1.6"/><path d="M7 5.5 L8.8 5.5 L9.4 8 L8.3 9 Q9.2 11 11 11.8 L12 10.7 L14.5 11.3 L14.5 13 Q10 13.6 7.4 10 Q6.4 8 7 5.5Z" fill="#fff"/></svg>
      <span>020 7946 0321</span>
      <span class="gap"></span>
      <svg width="20" height="20" viewBox="0 0 20 20"><circle cx="10" cy="10" r="9" fill="none" stroke="#fff" stroke-width="1.6"/><ellipse cx="10" cy="10" rx="4" ry="9" fill="none" stroke="#fff" stroke-width="1.3"/><line x1="1" y1="10" x2="19" y2="10" stroke="#fff" stroke-width="1.3"/></svg>
      <span style="font-size:15px">www.vta.co.uk</span>
    </div>
  </header>

  <section class="intro">
    <div class="intro__copy">
      <p>vTa is a leading and award winning network service provider specialising in delivering cloud solutions for voice, data and IT security.</p>
      <p class="justify">Our network, communications and computing platforms, combined with our committed service, will let your business applications run more smoothly, securely and continuously. We provide UK organisations with whole of market site-to-site connectivity, Internet access, hosted telephony, virtualisation and direct connections to public clouds. We tailor our services to create a solution to meet your business requirements and budget.</p>
      <p>Our UK-based Network Operations Centre proactively monitors your services 24/7/365.</p>
    </div>
    <div class="intro__visual" role="img" aria-label="Photograph of a businessman holding a glowing blue cloud of connected devices in his hands"></div>
  </section>

  <div class="rule" style="top:546px"></div>

  <h1 class="headline">
    <span class="your">YOUR</span>
    <span class="cloud">CLOUD</span>
    <span class="delivery">DELIVERY</span>
    <span class="partner">PARTNER</span>
  </h1>
  <div class="headline-divider"></div>

  <svg class="network-map" width="846" height="1200" viewBox="0 0 846 1200" aria-label="vTa network diagram">
    <defs>
      <symbol id="cloud" viewBox="0 0 100 50">
        <path d="M12 46 Q2 46 3 38 Q4 30 14 31 Q14 20 27 20 Q32 6 50 7 Q66 8 70 22 Q82 18 86 30 Q98 31 97 39 Q96 46 88 46 Z" fill="#fff" stroke="#b9bec3" stroke-width="1.4"/>
      </symbol>
      <symbol id="site" viewBox="0 0 48 48">
        <circle cx="24" cy="24" r="22" fill="#fff" stroke="var(--brand-blue)" stroke-width="2.4"/>
        <circle cx="24" cy="24" r="17" fill="#eaf3f8"/>
      </symbol>
    </defs>

    <g stroke="var(--line-grey)" stroke-width="1">
      <line x1="470" y1="600" x2="553" y2="678"/>
      <line x1="415" y1="640" x2="508" y2="694"/>
      <line x1="406" y1="708" x2="492" y2="724"/>
      <line x1="413" y1="762" x2="489" y2="759"/>
      <line x1="462" y1="818" x2="530" y2="789"/>
      <line x1="587" y1="798" x2="592" y2="840"/>
      <line x1="626" y1="681" x2="651" y2="642"/>
      <line x1="669" y1="705" x2="702" y2="684"/>
      <line x1="673" y1="748" x2="732" y2="756"/>
      <line x1="640" y1="782" x2="697" y2="813"/>
    </g>

    <ellipse cx="581" cy="736" rx="92" ry="62" fill="#fff" stroke="var(--brand-blue)" stroke-width="4"/>
    <text x="581" y="717" font-family="Roboto, Arial, sans-serif" font-size="22" fill="var(--ink)" text-anchor="middle">vTa</text>
    <text class="node-label" x="581" y="739" font-size="11.5">Network</text>
    <text class="node-label" x="581" y="754" font-size="11.5">Enterprise WAN</text>

    <!-- Sites -->
    <g>
      <use href="#site" x="446" y="559" width="42" height="42"/>
      <rect x="459" y="569" width="16" height="22" fill="var(--brand-blue)"/>
      <g fill="#fff"><rect x="462" y="572" width="3" height="3"/><rect x="469" y="572" width="3" height="3"/><rect x="462" y="578" width="3" height="3"/><rect x="469" y="578" width="3" height="3"/><rect x="462" y="584" width="3" height="3"/><rect x="469" y="584" width="3" height="3"/></g>
      <text class="node-label" x="467" y="613">Head Office</text>
    </g>
    <g>
      <use href="#site" x="376" y="605" width="42" height="42"/>
      <path d="M386 627 L397 616 L408 627 L405 627 L405 637 L389 637 L389 627 Z" fill="var(--brand-blue)"/>
      <rect x="394" y="630" width="5" height="7" fill="#fff"/>
      <text class="node-label" x="397" y="658">Home office</text>
    </g>
    <g>
      <use href="#site" x="364" y="678" width="42" height="42"/>
      <rect x="376" y="688" width="11" height="22" fill="var(--brand-blue)"/>
      <rect x="387" y="696" width="10" height="14" fill="var(--brand-blue)"/>
      <text class="node-label" x="385" y="731">Branch Office</text>
    </g>
    <g>
      <use href="#site" x="371" y="739" width="42" height="42"/>
      <rect x="385" y="749" width="13" height="22" rx="2" fill="var(--brand-blue)"/>
      <rect x="387" y="752" width="9" height="14" fill="#fff"/>
      <text class="node-label" x="392" y="793">Mobile working</text>
    </g>
    <g>
      <use href="#site" x="423" y="806" width="42" height="42"/>
      <rect x="437" y="815" width="14" height="24" fill="var(--brand-blue)"/>
      <g stroke="#fff" stroke-width="1"><line x1="439" y1="820" x2="449" y2="820"/><line x1="439" y1="825" x2="449" y2="825"/><line x1="439" y1="830" x2="449" y2="830"/><line x1="439" y1="835" x2="449" y2="835"/></g>
      <text class="node-label" x="444" y="864">Data Centre</text>
    </g>

    <!-- Clouds -->
    <use href="#cloud" x="633" y="587" width="78" height="39"/>
    <text class="partner-name" x="671" y="616">Tessvia</text>
    <text class="node-label" x="671" y="638">Private Cloud</text>

    <use href="#cloud" x="700" y="650" width="92" height="46"/>
    <text class="partner-name" x="746" y="675">nimbra data works</text>
    <text class="partner-name" x="746" y="685">Quellon Skyview</text>
    <text class="node-label" x="746" y="706">Public Cloud</text>

    <use href="#cloud" x="726" y="735" width="52" height="26"/>
    <text class="node-label" x="752" y="756">SaaS</text>

    <use href="#cloud" x="689" y="796" width="66" height="33"/>
    <text class="node-label" x="722" y="812">Cloud</text>
    <text class="node-label" x="722" y="822">Telephony</text>

    <use href="#cloud" x="518" y="812" width="152" height="76"/>
    <text class="node-label" x="600" y="859" font-size="11">Public Internet</text>
  </svg>

  <section class="highlights">
    <ul class="col-a">
      <li>Carrier-independent connectivity</li>
      <li>End-to-end converged networks</li>
      <li>UK-based proactive monitoring</li>
      <li>30+ points of presence</li>
      <li>ISO 9001 / ISO 27001 / ISO 20000</li>
    </ul>
    <ul class="col-b">
      <li>Over 15 years of service</li>
      <li>Public and Private cloud expertise</li>
      <li>Choice of security technologies (DDoS, Firewalls, VPNs)</li>
      <li>24/7 NOC</li>
      <li>Over 500 customers</li>
    </ul>
  </section>

  <footer class="footer">
    <div class="footer__item small">
      <svg width="14" height="14" viewBox="0 0 14 14"><circle cx="7" cy="4" r="3" fill="#fff"/><path d="M1 14 Q1 8 7 8 Q13 8 13 14Z" fill="#fff"/></svg>
      <span>Salesman</span>
    </div>
    <div class="footer__item small">
      <svg width="10" height="16" viewBox="0 0 10 16"><rect x="1" y="1" width="8" height="14" rx="1.5" fill="none" stroke="#fff" stroke-width="1.5"/><rect x="3" y="12" width="4" height="1.3" fill="#fff"/></svg>
      <span>020 7946 0321</span>
    </div>
    <div class="footer__item large">
      <svg width="26" height="16" viewBox="0 0 26 16"><rect x="3" y="1" width="22" height="14" fill="none" stroke="#fff" stroke-width="1.4"/><path d="M3 1 L14 9 L25 1" fill="none" stroke="#fff" stroke-width="1.4"/><line x1="0" y1="6" x2="3" y2="6" stroke="#fff"/><line x1="0" y1="10" x2="3" y2="10" stroke="#fff"/></svg>
      <span>info@vta.co.uk</span>
    </div>
    <div class="footer__item large">
      <svg width="12" height="17" viewBox="0 0 12 17"><path d="M6 16 Q0 8 0 6 A6 6 0 0 1 12 6 Q12 8 6 16Z" fill="#fff"/><circle cx="6" cy="6" r="2.2" fill="var(--brand-blue)"/></svg>
      <span>vTa, 12 Arden Row, London, E9 4PL</span>
    </div>
    <div class="footer__item large">
      <svg width="14" height="14" viewBox="0 0 14 14"><circle cx="7" cy="7" r="6" fill="#fff"/></svg>
      <span>chirpline.com/vTa</span>
    </div>
  </footer>

</main>
</body>
</html>
```